label design for cannabis

label template 4"x5.5" for a Massachusetts cannabis beverage product. labels will be transparent and placed on a blue (pantone 306C) bag.
https://www.drizzlepods.com/

Target Market(s)

cannabis customers in MA, 21+

Industry/Entity Type

cannabis consumer product

Font styles to use
Other font styles liked:
• DIN

Colors
0094D4
00A9DD
6FCCEA
C7EBF8
E9F6FB

Requirements
Must have
• label design with fizz logo, flavor (lemon, lime, plain, and coffee). 306C pantone for background and 11-0601 TCX for text. font=DINackground.
Nice to have
• tray icon, illustrated ice cubes in white (clear), yellow (lemon), green (lime) and brown (coffee)
Should not have
• no cartoonish characters

```html
<!DOCTYPE html>
<html lang="en">
<head>
<meta charset="utf-8">
<title>fizz infused ice cubes – label set</title>
<link rel="stylesheet" href="https://fonts.googleapis.com/css2?family=Barlow+Condensed:wght@500;600&family=Barlow+Semi+Condensed:wght@500;600&display=swap">
<style>
  :root {
    --label-blue: #13b5e5;
    --badge-navy: #1f3368;
    --text-white: #ffffff;
    --flavor-clear: #ffffff;
    --flavor-lemon: #f0e614;
    --flavor-lime: #8dc63f;
    --flavor-coffee: #a38b7f;
  }
  * { box-sizing: border-box; margin: 0; padding: 0; }
  html, body {
    width: 1200px; height: 1200px; overflow: hidden; background: #ffffff;
  }
  .label-sheet { position: relative; width: 1200px; height: 1200px; }
  .label {
    position: absolute; width: 411px; height: 564px;
    background: var(--label-blue);
    color: var(--text-white);
  }
  .label--clear  { left: 151px; top: 19px;  --flavor: var(--flavor-clear); }
  .label--lemon  { left: 646px; top: 19px;  --flavor: var(--flavor-lemon); }
  .label--lime   { left: 151px; top: 623px; --flavor: var(--flavor-lime); }
  .label--coffee { left: 646px; top: 623px; --flavor: var(--flavor-coffee); }

  .label__frame {
    position: absolute; inset: 17px;
    border: 2.5px solid var(--text-white);
    border-radius: 19px;
  }
  .brand {
    position: absolute; left: 0; right: 0; top: 62px;
    text-align: center;
    font-family: "Barlow Condensed", sans-serif;
    font-weight: 600; font-size: 108px; line-height: 1;
    letter-spacing: 1px;
  }
  .brand__tagline {
    position: absolute; left: 0; right: 0; top: 154px;
    text-align: center;
    font-family: "Barlow Condensed", sans-serif;
    font-weight: 500; font-size: 29px; line-height: 1;
  }
  .flavor-badge {
    position: absolute; left: 111px; top: 202px;
    width: 190px; height: 190px; border-radius: 50%;
    background: var(--badge-navy);
    border: 2.5px solid var(--text-white);
  }
  .flavor-badge__art {
    position: absolute; left: 22px; top: 8px; width: 142px; height: 128px;
    border-radius: 50% 50% 40% 40%;
    background: var(--badge-navy);
  }
  .flavor-badge__rule {
    position: absolute; left: 47px; top: 148px; width: 93px; height: 1.5px;
    background: var(--flavor);
  }
  .flavor-badge__name {
    position: absolute; left: 0; right: 0; top: 150px;
    text-align: center; color: var(--flavor);
    font-family: "Barlow Semi Condensed", sans-serif;
    font-weight: 600; font-size: 21px; letter-spacing: 1.5px;
  }
  .dose-tray {
    position: absolute; left: 114px; top: 459px; width: 184px; height: 52px;
  }
  .dose-tray__text {
    position: absolute; left: 0; right: 0; top: 1px;
    text-align: center;
    font-family: "Barlow Semi Condensed", sans-serif;
    font-weight: 500; font-size: 14px; letter-spacing: 0.6px; line-height: 20px;
  }
  .dose-tray svg { position: absolute; inset: 0; }
</style>
</head>
<body>
<main class="label-sheet">

  <section class="label label--clear">
    <div class="label__frame"></div>
    <h1 class="brand">fizz.</h1>
    <p class="brand__tagline">infused ice cubes</p>
    <div class="flavor-badge">
      <div class="flavor-badge__art" role="img" aria-label="Three outlined ice cubes in white"></div>
      <div class="flavor-badge__rule"></div>
      <p class="flavor-badge__name">clear</p>
    </div>
    <div class="dose-tray">
      <svg viewBox="0 0 184 52" fill="none" stroke="#ffffff" stroke-width="2">
        <rect x="1" y="1" width="182" height="21"/>
        <path d="M6 22 L9 49 H33 L36 22 M41 22 L44 49 H68 L71 22 M76 22 L79 49 H103 L106 22 M111 22 L114 49 H138 L141 22 M146 22 L149 49 H173 L176 22"/>
      </svg>
      <p class="dose-tray__text">50 mg per tray</p>
    </div>
  </section>

  <section class="label label--lemon">
    <div class="label__frame"></div>
    <h1 class="brand">fizz.</h1>
    <p class="brand__tagline">infused ice cubes</p>
    <div class="flavor-badge">
      <div class="flavor-badge__art" role="img" aria-label="Three outlined ice cubes in yellow"></div>
      <div class="flavor-badge__rule"></div>
      <p class="flavor-badge__name">lemon</p>
    </div>
    <div class="dose-tray">
      <svg viewBox="0 0 184 52" fill="none" stroke="#ffffff" stroke-width="2">
        <rect x="1" y="1" width="182" height="21"/>
        <path d="M6 22 L9 49 H33 L36 22 M41 22 L44 49 H68 L71 22 M76 22 L79 49 H103 L106 22 M111 22 L114 49 H138 L141 22 M146 22 L149 49 H173 L176 22"/>
      </svg>
      <p class="dose-tray__text">50 mg per tray</p>
    </div>
  </section>

  <section class="label label--lime">
    <div class="label__frame"></div>
    <h1 class="brand">fizz.</h1>
    <p class="brand__tagline">infused ice cubes</p>
    <div class="flavor-badge">
      <div class="flavor-badge__art" role="img" aria-label="Three outlined ice cubes in green"></div>
      <div class="flavor-badge__rule"></div>
      <p class="flavor-badge__name">lime</p>
    </div>
    <div class="dose-tray">
      <svg viewBox="0 0 184 52" fill="none" stroke="#ffffff" stroke-width="2">
        <rect x="1" y="1" width="182" height="21"/>
        <path d="M6 22 L9 49 H33 L36 22 M41 22 L44 49 H68 L71 22 M76 22 L79 49 H103 L106 22 M111 22 L114 49 H138 L141 22 M146 22 L149 49 H173 L176 22"/>
      </svg>
      <p class="dose-tray__text">50 mg per tray</p>
    </div>
  </section>

  <section class="label label--coffee">
    <div class="label__frame"></div>
    <h1 class="brand">fizz.</h1>
    <p class="brand__tagline">infused ice cubes</p>
    <div class="flavor-badge">
      <div class="flavor-badge__art" role="img" aria-label="Three outlined ice cubes in brown"></div>
      <div class="flavor-badge__rule"></div>
      <p class="flavor-badge__name">coffee</p>
    </div>
    <div class="dose-tray">
      <svg viewBox="0 0 184 52" fill="none" stroke="#ffffff" stroke-width="2">
        <rect x="1" y="1" width="182" height="21"/>
        <path d="M6 22 L9 49 H33 L36 22 M41 22 L44 49 H68 L71 22 M76 22 L79 49 H103 L106 22 M111 22 L114 49 H138 L141 22 M146 22 L149 49 H173 L176 22"/>
      </svg>
      <p class="dose-tray__text">50 mg per tray</p>
    </div>
  </section>

</main>
</body>
</html>
```